Makeup Artist Requires Business Card design

Hi

I am looking for a business card design to market my makeup artist business. I operate under my own name Mara Veldt and I would like to keep the design of the card very simplistic and chic - something that keeps both my name and profession (makeup artist) the focus of the card. I would like it to be a style that is eyecatching to the reader (i am open to anything unusual) but upmarket.

Target Market(s)

women, magazine/beauty/fashion editors, photographers.

Industry/Entity Type

Business

Requirements
Must have
• Must contain:

Phone number: 0418 372 915
Website: www.maraveldt.com.au
email: contact@maraveldt.com.au

(although you don't need to have prefaced these with the words phone number, website etc :))
Should not have
• I am not looking for anything overly colorful - my preference is to keep the card dark if possible.

```html
<!DOCTYPE html>
<html lang="en">
<head>
<meta charset="utf-8">
<title>Business card presentation :: Mara Veldt - makeup artist</title>
<link rel="stylesheet" href="https://fonts.googleapis.com/css2?family=Bodoni+Moda:wght@400&family=Roboto:wght@300&display=swap">
<style>
  :root {
    --page-bg: #ffffff;
    --caption-grey: #8a8a8a;
    --card-plum: #78003a;
    --card-ink: #ffffff;
    --art-light: #f6eef2;
  }
  * { margin: 0; padding: 0; box-sizing: border-box; }
  html, body {
    width: 1200px;
    height: 849px;
    overflow: hidden;
    background: var(--page-bg);
  }
  .sheet {
    position: relative;
    width: 1200px;
    height: 849px;
    font-family: "Roboto", Helvetica, Arial, sans-serif;
    font-weight: 300;
  }
  .sheet-title {
    position: absolute;
    left: 51px;
    top: 46px;
    font-size: 19px;
    color: var(--caption-grey);
    letter-spacing: 0.01em;
    white-space: nowrap;
  }
  .card {
    position: absolute;
    left: 305px;
    top: 250px;
    width: 588px;
    height: 347px;
    background: var(--card-plum);
    color: var(--card-ink);
    box-shadow: 0 1px 6px rgba(0, 0, 0, 0.35);
    overflow: hidden;
  }
  .card-art {
    position: absolute;
    left: 0;
    top: 0;
    width: 190px;
    height: 100%;
    background: linear-gradient(90deg, var(--art-light) 0%, var(--art-light) 45%, var(--card-plum) 100%);
  }
  .card-divider {
    position: absolute;
    left: 244px;
    top: 42px;
    width: 1px;
    height: 263px;
    background: var(--card-ink);
  }
  .card-name {
    position: absolute;
    left: 259px;
    top: 34px;
    font-family: "Bodoni Moda", "Didot", serif;
    font-weight: 400;
    font-size: 76px;
    line-height: 65px;
    letter-spacing: 0.03em;
  }
  .card-name span { display: block; }
  .card-profession {
    position: absolute;
    left: 268px;
    top: 166px;
    font-size: 13px;
    letter-spacing: 0.52em;
    white-space: nowrap;
  }
  .card-contacts {
    position: absolute;
    top: 238px;
    font-size: 19px;
    line-height: 24.5px;
    letter-spacing: 0.02em;
    white-space: nowrap;
  }
  .card-contacts.labels { right: 360px; text-align: right; }
  .card-contacts.values { left: 260px; }
  .sheet-caption {
    position: absolute;
    left: 305px;
    top: 645px;
    font-size: 12px;
    color: var(--caption-grey);
  }
</style>
</head>
<body>
  <main class="sheet">
    <p class="sheet-title">business card presentation &nbsp;::&nbsp; Mara Veldt - makeup artist</p>

    <section class="card" aria-label="Business card front">
      <div class="card-art" role="img" aria-label="Stylised white illustration of a woman's face in profile with long lashes and full lips"></div>
      <div class="card-divider"></div>
      <h1 class="card-name"><span>Mara</span><span>Veldt</span></h1>
      <p class="card-profession">makeup artist</p>
      <div class="card-contacts labels">
        <p>call</p>
        <p>web</p>
        <p>email</p>
      </div>
      <div class="card-contacts values">
        <p>0418 372 915</p>
        <p>www.maraveldt.com.au</p>
        <p>contact@maraveldt.com.au</p>
      </div>
    </section>

    <p class="sheet-caption">business card dimensions: 85mm wide x 50mm high</p>
  </main>
</body>
</html>
```